Business Card Design Project

We are looking to redesign the logo, business card and stationary of one of our group companies - KESTRAL SUPPLY COMPANY LLC.

The company specialises in industrial PVC and CPVC Piping systems. It is situated in the Middle East and the focus is purely in this region.

The logo work is already completed. The file is uploaded for the reference.

We are looking for a clean minimalistic design for the business card.

regards
Ormund
Updates

Hello Everyone!

Thanks for submitting your designs. 

Yet to find the right design. Probably the below links will give you guys some more idea on what we would like.

Minimalist design with some creativity.

Ormund

http://plaincardgallery.example/inspiration/15-beautifully-minimal-business-cards

http://www.quietlayouthub.example/2011/11/14/30-minimalist-business-card-design/

http://www.firmpixelnotes.example/inspiration/minimal-business-cards/

Target Market(s)

Industrial users

Industry/Entity Type

Industrial

Requirements
Must have
• - Minimalistic design

- Back side of the card should include the manufacturer BRAVOLINE CANADA's decal. The file is upload for the reference

- Further information
Company Name:
KESTRAL SUPPLY COMPANY LLC
Address:
PO Box 9087, Sharjah Industrial Area 5, Qutrani Road
Sharjah, United Arab Emirates
Telephone:
+971-6-5018-392
Fax:
+977-6-5018-393
Email:
mail@ksc-holding.example

- FYI, Kestral Supply Company LLC is the authorised distributor for BRAVOLINE CANADA in the UAE. For further information on bravoline please visit the website www.bravoline.example

```html
<!DOCTYPE html>
<html lang="en">
<head>
<meta charset="utf-8">
<title>Kestral Supply Company LLC – Business Card</title>
<link href="https://fonts.googleapis.com/css2?family=Arimo:wght@700&display=swap" rel="stylesheet">
<style>
  :root {
    --brand-blue: #3a7fc9;
    --contact-blue: #1f5fb5;
    --address-grey: #6b6b6b;
    --paper: #f7f7f7;
    --fitting-light: #e9e9e9;
    --fitting-mid: #dcdcdc;
  }
  html, body {
    margin: 0;
    padding: 0;
    overflow: hidden;
    background: #ffffff;
  }
  .card {
    position: relative;
    width: 1200px;
    height: 686px;
    overflow: hidden;
    background: var(--paper);
    font-family: "Arimo", Arial, sans-serif;
    font-weight: 700;
  }
  .card__backdrop {
    position: absolute;
    inset: 0;
    width: 100%;
    height: 100%;
  }
  .company-name {
    position: absolute;
    left: 100px;
    top: 126px;
    width: 560px;
    margin: 0;
    text-align: center;
    font-size: 52px;
    line-height: 62px;
    letter-spacing: 0.5px;
    color: var(--brand-blue);
    text-shadow: 3px 5px 6px rgba(0, 0, 0, 0.25);
  }
  .address {
    position: absolute;
    right: 40px;
    top: 277px;
    margin: 0;
    font-style: normal;
    text-align: right;
    font-size: 25px;
    line-height: 34.3px;
    color: var(--address-grey);
  }
  .phones {
    position: absolute;
    right: 40px;
    top: 452px;
    margin: 0;
    padding: 0;
    list-style: none;
    text-align: right;
    font-size: 29px;
    line-height: 40px;
    color: var(--contact-blue);
  }
  .brand-mark {
    position: absolute;
    left: 0;
    width: 1200px;
    top: 552px;
    display: flex;
    justify-content: center;
    align-items: center;
    gap: 10px;
    font-size: 20px;
    color: var(--contact-blue);
  }
  .brand-mark__square {
    width: 18px;
    height: 18px;
    background: var(--contact-blue);
  }
  .email {
    position: absolute;
    left: 0;
    width: 1200px;
    top: 626px;
    text-align: center;
    font-size: 25px;
    color: var(--contact-blue);
  }
</style>
</head>
<body>
  <div class="card">
    <svg class="card__backdrop" viewBox="0 0 1200 686" role="img" aria-label="Faded photograph of PVC pipe fittings and flanges filling the card background">
      <defs>
        <radialGradient id="fittingGlow" cx="0.6" cy="0.55" r="0.7">
          <stop offset="0" stop-color="var(--fitting-mid)"/>
          <stop offset="0.6" stop-color="var(--fitting-light)"/>
          <stop offset="1" stop-color="var(--paper)"/>
        </radialGradient>
      </defs>
      <rect width="1200" height="686" fill="url(#fittingGlow)"/>
    </svg>

    <h1 class="company-name">KESTRAL SUPPLY<br>COMPANY LLC</h1>

    <address class="address">
      PO Box 9087<br>
      Sharjah Industrial Area 5<br>
      Qutrani Road<br>
      Sharjah<br>
      United Arab Emirates
    </address>

    <ul class="phones">
      <li>+971-6-5018-392</li>
      <li>+977-6-5018-393</li>
    </ul>

    <div class="brand-mark">
      <span class="brand-mark__square"></span>
      <span class="brand-mark__name">Kestral Supply</span>
    </div>

    <div class="email">mail@ksc-holding.example</div>
  </div>
</body>
</html>
```